PITCH PRESENTATION for Feature Film Project

A while ago I had some key art designed for me for a film project called Ember Crane's Oath (I see it's still in the online portfolio for pixelorchard, who did the original work). I'm now taking that project to a series of pitch meetings at a film festival here in Canada and am putting together a powerpoint presentation.
I would want you to use the original design/aesthetic framework across the 14 pages of the presentation. I have provided the text and some image ideas (there's also one video to insert) that you may or may not use, etc. Probably for a large chunk of the pages - perhaps 6 of the ten - you could just clean it up and create a common background theme on which to place the companion text. Obviously, while making it pretty is a priority, it's also a priority for it to be legible to the people whom I'm pitching the project when it is projected onto a large screen.
I've uploaded a draft of the powerpoint text - there could be some minor changes between now and next week. I'll be leaving for the festival on December 3 so, obviously need a final version before that date. I've attached a .jpg of the original artwork along with the powerpoint.

Let me know if you need more details.
Updates

I wasn't able to upload the .psd file of the original poster artwork with layers & fonts but here is a link to download it from my dropbox: https://www.filevaultly.net/s/k3p8tqzr1mw4xa/FA-Ember%20Crane%27s%20Oath%20poster.psd?dl=0 best Derek

Target Market(s)

This is targeted at some Chinese studio executives to whom the project will be pitched. It is for a film that is a martial arts thriller.

Industry/Entity Type

Festival

Requirements
Must have
• The main thing is to use the already-existing material (the poster - incl colour scheme and fonts) as the aesthetic foundation for the presentation. We are, in a sense, trying to strengthen the brand identity of the project with the execs.

```html
<!DOCTYPE html>
<html lang="en">
<head>
<meta charset="utf-8">
<title>Ember Crane's Oath — Pitch Slide</title>
<link rel="stylesheet" href="https://fonts.googleapis.com/css2?family=Crimson+Pro:wght@400;500&display=swap">
<style>
  :root {
    --ink-deep: #120c08;
    --ink-mid: #2a1e14;
    --sepia: #5a4632;
    --ember: #ec8a1c;
    --paper: #f4efe6;
    --still-top: #6f7c84;
    --still-mid: #8fa9b0;
    --still-low: #6b5a3e;
  }
  * { margin: 0; padding: 0; box-sizing: border-box; }
  html, body {
    width: 1200px;
    height: 675px;
    overflow: hidden;
    background: var(--ink-deep);
  }
  .slide {
    position: relative;
    width: 1200px;
    height: 675px;
    overflow: hidden;
    font-family: "Crimson Pro", "Georgia", serif;
  }
  .slide-backdrop {
    position: absolute;
    inset: 0;
    background:
      radial-gradient(ellipse 520px 420px at 420px 330px, rgba(120, 92, 64, 0.55), transparent 70%),
      radial-gradient(ellipse 300px 260px at 120px 600px, rgba(90, 70, 50, 0.45), transparent 70%),
      linear-gradient(180deg, var(--ink-mid) 0%, var(--sepia) 55%, var(--ink-mid) 100%);
  }
  .slide-vignette {
    position: absolute;
    inset: 0;
    background: radial-gradient(ellipse 760px 520px at 50% 50%, transparent 40%, rgba(0, 0, 0, 0.75) 100%);
  }
  .slide-title {
    position: absolute;
    top: 22px;
    left: 0;
    width: 1200px;
    text-align: center;
    color: var(--ember);
    font-size: 67px;
    font-weight: 400;
    line-height: 1.1;
  }
  .logline {
    position: absolute;
    top: 162px;
    right: 557px;
    width: 560px;
    text-align: right;
    color: var(--paper);
    font-size: 37px;
    line-height: 45px;
    font-weight: 400;
  }
  .film-still {
    position: absolute;
    left: 720px;
    top: 147px;
    width: 342px;
    height: 503px;
    background: linear-gradient(180deg, var(--still-top) 0%, var(--still-mid) 40%, var(--still-low) 80%, #c9c2b4 100%);
    border: 2px solid rgba(255, 255, 255, 0.08);
  }
</style>
</head>
<body>
  <main class="slide">
    <div class="slide-backdrop" role="img" aria-label="Dark sepia textured backdrop with a faint photograph of the heroine"></div>
    <div class="slide-vignette"></div>
    <h1 class="slide-title">Ember Crane's Oath</h1>
    <p class="logline">A widow's act of vengeance<br>brings the wrath of both<br>the Triad and the police<br>down upon her and her<br>loved ones.</p>
    <div class="film-still" role="img" aria-label="Film still of the heroine standing in a dojo holding a sword, wearing a light blue top and patterned trousers"></div>
  </main>
</body>
</html>
```